Website for a web design agency

We are a website and marketing agency. We do website design, development, and well as Brindle and Quorvia advertising and analytics. We ourselves need a new website for our own brand. We are working on some designs in-house with our own designers, but we also wanted to see what outside designers would come up with.
We are starting off with the homepage, and here is the breakdown of the sections:
https://files.brindlework.example/sheet/d/7kqTr2VnPLwXeHsaMcY4oBfJzuGNtKdWiEh3Rx9pLmQb/view?mode=share
This doc also has many links to sites we have done, which you can take screenshots of for the portfolio section.
In terms of the "look" I am going for, I want to look high-end and very beautiful designs. I found this website that I like a lot that you can use some of the elements of, just as a starting point:
http://velmarkstudio.example/layouts/pixelbarn/html/ostrevo/index.html and here is another design option they have http://velmarkstudio.example/layouts/pixelbarn/html/ostrevo/index-4.html
I'm also uploading my logo. The logo matches the gold and black look from these websites, but I would be open to switching to another color scheme if needed.
This is the link to my very old website, which you can use for some of the dummy text, and a pic of myself. I will be taking more pics of myself:
https://theplumtreeandwillowgroup.example/
We need a homepage and a portfolio page right now, but if you are the winner, we will be hiring you to make additional pages.
Updates
More designs continue to come in even today, and I want to make sure no other designers are still submitting designs.
Target Market(s)
medium and large businesses owners, and non-profits
Number of Pages Required
1 page

```html
<!DOCTYPE html>
<html lang="en">
<head>
<meta charset="utf-8">
<title>Vordale Studio – Enterprise Web Development</title>
<link rel="stylesheet" href="https://fonts.googleapis.com/css2?family=Archivo:wght@400;600;700;800;900&family=Lato:wght@400;700&family=Comfortaa:wght@500;700&display=swap">
<style>
:root{
  --ink:#1f1f1d;
  --panel:#3a3a36;
  --card:#33332f;
  --form:#2a2a27;
  --gold:#f2b21d;
  --white:#ffffff;
  --muted:#c4c4c0;
  --ghost:#3c3c38;
  --ghost-light:#4a4a45;
  --photo:#6d6a64;
  --head:'Archivo',sans-serif;
  --body:'Lato',sans-serif;
}
*{margin:0;padding:0;box-sizing:border-box}
html,body{width:1200px;height:5204px;overflow:hidden}
body{position:relative;background:var(--ink);color:var(--white);font-family:var(--body)}
.abs{position:absolute}
.band{position:absolute;left:0;width:1200px}
.band-dark{background:var(--ink)}
.band-panel{background:var(--panel)}
.h-title{font-family:var(--head);font-weight:900;font-size:31px;letter-spacing:.5px;text-transform:uppercase}
.eyebrow{font-size:12px;color:var(--muted);display:flex;align-items:center;gap:10px}
.eyebrow::before{content:"";width:60px;height:1px;background:var(--gold)}
.ghost-word{position:absolute;font-family:var(--head);font-weight:900;color:var(--ghost);text-transform:uppercase;white-space:nowrap;line-height:1}
.photo{background:linear-gradient(135deg,#7a766f,#4f4c47)}
.btn-outline{position:absolute;border:2px solid var(--white);font-family:var(--head);font-weight:700;font-size:12px;letter-spacing:1px;display:flex;align-items:center;justify-content:center;color:var(--white)}
.more{font-family:var(--head);font-weight:800;font-size:12px;letter-spacing:.5px;display:flex;align-items:center;gap:12px}
.more i{width:15px;height:15px;background:var(--white);display:inline-block;position:relative}
.more i::after{content:"+";position:absolute;inset:0;color:var(--ink);font-style:normal;font-size:13px;line-height:15px;text-align:center;font-weight:900}

/* header */
.site-header{top:0;height:75px;background:var(--ink);border-bottom:1px solid #333}
.logo{font-family:var(--head);font-weight:900;color:var(--gold);font-size:21px;letter-spacing:.5px;line-height:1}
.logo small{display:block;font-size:8px;letter-spacing:4px;font-weight:700;margin-top:2px}
.nav{position:absolute;left:458px;top:31px;display:flex;gap:48px;font-family:var(--head);font-size:11px;font-weight:600;letter-spacing:.5px}
.nav a{color:var(--white);text-decoration:none;position:relative}
.nav a.active::after{content:"";position:absolute;left:0;top:20px;width:26px;height:2px;background:var(--gold)}
.hdr-box{position:absolute;top:26px;width:22px;height:22px;border:1px solid var(--gold)}

/* hero */
.hero-title{left:224px;top:175px;font-family:var(--head);font-weight:900;font-size:60px;line-height:68px}
.hero-title .gold{color:var(--gold)}
.hero-sub{left:224px;top:396px;font-size:13px;line-height:20px;color:var(--white)}
.video{left:491px;top:168px;width:600px;height:339px}
.video-name{left:502px;top:390px;font-family:'Comfortaa',sans-serif;font-weight:700;font-size:32px;line-height:34px;color:var(--white);text-align:center;width:300px}
.play{left:771px;top:323px;width:30px;height:30px;border-radius:50%;background:var(--gold)}
.play::after{content:"";position:absolute;left:12px;top:9px;border-left:9px solid #fff;border-top:6px solid transparent;border-bottom:6px solid transparent}
.fullscreen{left:957px;top:485px;width:108px;height:46px;background:var(--white);color:var(--ink);font-size:11px;font-weight:700;display:flex;align-items:center;padding-left:26px}
.fs-btn{left:1065px;top:485px;width:46px;height:46px;background:var(--gold);display:flex;align-items:center;justify-content:center}
.fs-btn span{width:20px;height:20px;border-radius:50%;background:#fff;display:block}

/* services */
.section-center{left:0;width:1200px;text-align:center}
.sub-gold{color:var(--gold);font-size:11px;letter-spacing:1px;font-family:var(--head);font-weight:600}
.title-rule{width:130px;height:2px;background:var(--gold);margin:10px auto 12px}
.svc{position:absolute;width:228px;height:252px;background:var(--card);padding:28px 32px}
.svc.gold{background:var(--gold)}
.svc .num{font-family:var(--head);font-weight:700;font-size:13px;display:flex;align-items:center;gap:10px}
.svc .num::after{content:"";width:32px;height:2px;background:var(--white)}
.svc.gold .num::after{background:var(--ink)}
.svc h3{font-family:var(--head);font-weight:700;font-size:17px;margin:18px 0 14px;line-height:22px}
.svc p{font-size:12.5px;line-height:18px;color:var(--muted);margin-bottom:24px}
.svc.gold,.svc.gold p{color:var(--ink)}
.svc.gold .more i{background:var(--ink)}
.svc.gold .more i::after{color:var(--gold)}
.corner{position:absolute;border-color:var(--gold);border-style:solid}

/* about */
.about-copy{left:681px;width:330px}
.about-copy h2{font-family:var(--head);font-weight:900;font-size:27px;line-height:42px}
.about-copy p{font-size:12.5px;line-height:18px;color:var(--muted);margin-top:18px}

/* portfolio */
.shot{position:absolute;background:linear-gradient(160deg,#e9e7e2,#a9a6a0)}
.dots{position:absolute;display:flex;gap:6px;align-items:center}
.dots span{width:4px;height:4px;background:#fff;border-radius:50%}
.dots span.on{width:14px;height:3px;border-radius:0;background:var(--gold)}

/* case studies */
.case{position:absolute;top:2608px;height:188px}
.case .txt{position:absolute;left:20px;right:14px;font-size:11px;line-height:16px;color:#f0f0f0}
.case .txt b{display:block;font-family:var(--head);font-size:12px;margin-bottom:6px;color:#fff}

/* stats */
.stats{top:2875px;height:127px;background:var(--gold);color:var(--ink)}
.stat{position:absolute;top:43px;display:flex;align-items:center;gap:14px}
.stat strong{font-family:var(--head);font-weight:900;font-size:40px}
.stat span{font-family:var(--head);font-weight:700;font-size:10.5px;letter-spacing:1px;line-height:14px}

/* help */
.help{position:absolute;top:3206px;width:228px;height:248px;background:var(--card);padding:38px 32px 0}
.help h3{font-family:var(--head);font-weight:800;font-size:16px;letter-spacing:.5px}
.help .big{position:absolute;right:18px;top:6px;font-family:var(--head);font-weight:900;font-size:62px;color:transparent;-webkit-text-stroke:2px #8f8f89;line-height:1}
.help p{font-size:12.5px;line-height:18.5px;color:var(--muted);margin-top:26px;height:114px}
.help .more{color:var(--gold);margin-top:22px}

/* testimonials */
.quote{left:281px;top:3727px;width:330px;font-size:12.5px;line-height:18.5px;color:#e6e6e2}
.qmark{left:224px;top:3722px;font-family:var(--head);font-weight:900;font-style:italic;font-size:34px;color:var(--gold);line-height:1}
.avatar{position:absolute;width:60px;height:60px}
.avatar.gold{outline:3px solid var(--gold);outline-offset:-3px}

/* team */
.member{position:absolute;top:4143px;width:228px;text-align:center}
.member .pic{height:248px;position:relative}
.member .soc{position:absolute;bottom:14px;left:50%;transform:translateX(-50%);display:flex;gap:4px;background:var(--gold);padding:4px}
.member .soc i{width:16px;height:16px;border:1px solid #fff;display:block}
.member h4{font-family:var(--head);font-weight:800;font-size:15px;margin-top:22px}
.member small{font-size:11.5px;color:var(--muted);display:block;margin-top:6px}

/* contact */
.contact{left:224px;top:4549px;width:750px;height:404px;background:var(--form)}
.contact h2{position:absolute;left:32px;top:30px;font-family:var(--head);font-weight:900;font-size:22px}
.contact .lead{position:absolute;left:32px;top:66px;font-size:11.5px;color:var(--muted)}
.field{position:absolute;border:1px solid #66665f;font-size:11px;color:#a8a8a2;padding:10px 12px}
.submit{position:absolute;left:32px;top:339px;width:124px;height:35px;background:var(--gold);color:var(--ink);font-family:var(--head);font-weight:800;font-size:11px;display:flex;align-items:center;justify-content:center}
.info{position:absolute;left:548px;top:0;width:202px;height:404px;background:var(--gold);color:var(--ink);padding:32px 30px;font-size:11.5px}
.info .row{position:absolute;left:30px;display:flex;gap:12px;line-height:17px}

/* footer */
.footer-col{position:absolute;top:5000px;font-size:12px;color:var(--muted);line-height:23px}
.footer-col h5{font-family:var(--head);font-weight:800;font-size:11px;color:#fff;margin-bottom:14px;letter-spacing:.5px}
.circle{width:22px;height:22px;border:1px solid #fff;border-radius:50%;display:inline-block}
</style>
</head>
<body>

<!-- Header -->
<header class="band site-header">
  <div class="abs logo" style="left:226px;top:22px">VORDALE<small>STUDIO</small></div>
  <nav class="nav"><a class="active">HOME</a><a>ABOUT</a><a>PORTFOLIO</a><a>CONTACT</a></nav>
  <div class="hdr-box" style="left:893px"></div>
  <div class="hdr-box" style="left:950px"></div>
</header>

<!-- Hero -->
<section>
  <h1 class="abs hero-title">WE<br><span class="gold">BUILD</span><br>VALUE</h1>
  <p class="abs hero-sub">Enterprise Level Website Development<br>and Online Marketing</p>
  <a class="btn-outline" style="left:224px;top:464px;width:170px;height:43px">SEE HOW WE DO IT</a>
  <div class="abs" style="left:1060px;top:150px;width:40px;height:80px;background:var(--gold);opacity:.35"></div>
  <div class="abs video photo" role="img" aria-label="Video still of the studio founder speaking to camera"></div>
  <div class="abs play"></div>
  <div class="abs video-name">Marcus Ellery<br>web developer</div>
  <div class="abs fullscreen">Full Screen</div>
  <div class="abs fs-btn"><span></span></div>
</section>

<!-- What we do -->
<div class="ghost-word" style="left:-6px;top:566px;font-size:84px">CODE</div>
<div class="ghost-word" style="left:866px;top:678px;font-size:84px">DESIGN</div>
<section class="abs section-center" style="top:628px">
  <h2 class="h-title">What We Do</h2>
  <div class="title-rule"></div>
  <div class="sub-gold">THINGS WE CRUSH</div>
</section>

<div class="corner" style="left:221px;top:745px;width:60px;height:100px;border-width:3px 0 0 3px"></div>
<article class="svc" style="left:224px;top:748px"><div class="num">01</div><h3>Websites</h3><p>Lorem ipsum dolor sit amet, consetetur sadipscing elitr, sed diam nonumy eirmod tempor</p><div class="more">KNOW MORE <i></i></div></article>
<article class="svc gold" style="left:485px;top:748px"><div class="num">02</div><h3>Landing Pages</h3><p>Lorem ipsum dolor sit amet, consetetur sadipscing elitr, sed diam nonumy eirmod tempor</p><div class="more">KNOW MORE <i></i></div></article>
<article class="svc" style="left:745px;top:748px"><div class="num">03</div><h3>Donation Pages</h3><p>Lorem ipsum dolor sit amet, consetetur sadipscing elitr, sed diam nonumy eirmod tempor</p><div class="more">KNOW MORE <i></i></div></article>
<article class="svc" style="left:224px;top:1034px"><div class="num">04</div><h3>PPC &amp; Funnels</h3><p>Lorem ipsum dolor sit amet, consetetur sadipscing elitr, sed diam nonumy eirmod tempor</p><div class="more">KNOW MORE <i></i></div></article>
<article class="svc" style="left:485px;top:1034px"><div class="num">05</div><h3>Video Marketing</h3><p>Lorem ipsum dolor sit amet, consetetur sadipscing elitr, sed diam nonumy eirmod tempor</p><div class="more">KNOW MORE <i></i></div></article>
<article class="svc" style="left:745px;top:1034px;padding-top:28px"><div class="num">06</div><h3 style="margin-bottom:8px">Analytics &amp;<br>Optimisation</h3><p style="margin-bottom:20px">Lorem ipsum dolor sit amet, consetetur sadipscing elitr, sed diam nonumy eirmod tempor</p><div class="more">KNOW MORE <i></i></div></article>
<div class="corner" style="left:917px;top:1188px;width:60px;height:100px;border-width:0 3px 3px 0"></div>

<!-- About -->
<section class="band band-panel" style="top:1380px;height:418px">
  <svg class="abs" style="left:150px;top:140px" width="300" height="280" viewBox="0 0 300 280">
    <path d="M8 280 V150 A142 142 0 0 1 150 8 H300 V70 H150 A80 80 0 0 0 70 150 V280 Z" fill="#f2b21d"/>
    <path d="M8 280 V150 A142 142 0 0 1 150 8 H300" fill="none" stroke="#1f1f1d" stroke-width="3" transform="translate(6 6)"/>
  </svg>
  <div class="abs photo" style="left:290px;top:8px;width:292px;height:410px;border-radius:140px 140px 0 0" role="img" aria-label="Portrait of the studio founder in a white shirt"></div>
  <div class="abs about-copy" style="top:42px">
    <div style="text-align:right;font-size:11px;color:var(--muted);width:300px">Designing Growth</div>
    <h2>WHAT DO YOU NEED<br>&amp; HOW WE DOING IT</h2>
    <p>Lorem ipsum dolor sit amet, consetetur sadipscing elitr, sed diam nonumy eirmod tempor invidunt ut labore et dolore magna aliquyam erat,</p>
    <p>Sed diam voluptua. At vero eos et accusam et justo duo dolores et ea rebum. Stet clita kasd</p>
  </div>
  <a class="btn-outline" style="left:681px;top:329px;width:138px;height:46px;font-size:11px">LEARN MORE</a>
</section>

<!-- Portfolio -->
<section class="band band-dark" style="top:1798px;height:683px">
  <div class="ghost-word" style="left:727px;top:92px;font-size:58px">OUR PORTFOLIO</div>
  <div class="abs eyebrow" style="left:310px;top:94px">10+ years Experience</div>
  <h2 class="abs h-title" style="left:224px;top:118px;font-size:29px">Recent Projects</h2>
  <div class="shot" style="left:0;top:232px;width:218px;height:279px" role="img" aria-label="Screenshot of an industrial company website"></div>
  <div class="shot" style="left:218px;top:232px;width:222px;height:279px" role="img" aria-label="Screenshot of a nonprofit landing page"></div>
  <div class="shot" style="left:440px;top:202px;width:313px;height:339px;background:linear-gradient(180deg,#fff 0 6%,#2b4c8f 6% 40%,#f4f4f4 40%)" role="img" aria-label="Screenshot of a film production company website"></div>
  <div class="shot" style="left:753px;top:232px;width:220px;height:279px" role="img" aria-label="Screenshot of an interior design gallery"></div>
  <div class="shot" style="left:973px;top:232px;width:227px;height:279px" role="img" aria-label="Screenshot of a smart mirror product page"></div>
  <div class="dots" style="left:573px;top:586px"><span></span><span class="on"></span><span></span><span></span></div>
</section>

<!-- Case studies -->
<section class="band band-panel" style="top:2481px;height:394px">
  <div class="abs eyebrow" style="left:710px;top:38px">Growing Businesses</div>
  <h2 class="abs h-title" style="left:621px;top:62px;font-size:28px">Latest Case Studies</h2>
</section>
<div class="case photo" style="left:0;width:259px" role="img" aria-label="Diagram-style case study graphic"><div class="txt" style="left:4px;bottom:14px">Lorem ipsum dolor sit amet, consectetur adipiscing elit in purus urna, maximus eu consequat.</div></div>
<div class="case photo" style="left:277px;width:313px" role="img" aria-label="Team working in a bright office"><div class="txt" style="bottom:14px"><b>Case Study Heading</b>Lorem ipsum dolor sit amet, consectetur adipiscing elit in purus urna, maximus eu consequat.</div></div>
<div class="case" style="left:608px;width:313px;background:linear-gradient(135deg,#4a4741,#2e2c29)" role="img" aria-label="Colleagues reviewing work at a laptop"><div class="txt" style="top:18px;left:36px;right:36px;font-size:11.5px"><b>Case Study Heading</b>Lorem ipsum dolor sit amet, consectetur adipiscing elit. In purus urna, maximus eu consequat non. Aliquam felis. Cras non urna quis metus gravida vestibulum sit amet id felis. Aliquam nec libero at mauris dictum efficitur.</div></div>
<div class="case photo" style="left:939px;width:261px" role="img" aria-label="Two people collaborating at a desk"><div class="txt" style="bottom:14px"><b>Case Study Heading</b>Lorem ipsum dolor sit amet, consectetur adipiscing elit in purus urna, maximus eu consequat.</div></div>
<div class="dots" style="left:573px;top:2838px"><span></span><span class="on"></span><span></span><span></span></div>

<!-- Stats -->
<section class="band stats">
  <svg class="abs" style="left:34px;top:86px" width="36" height="30" viewBox="0 0 36 30"><path d="M2 2 L34 10 L10 28 Z M2 2 L14 16" fill="none" stroke="#1f1f1d" stroke-width="2"/></svg>
  <div class="stat" style="left:224px"><strong>510</strong><span>HAPPY<br>CLIENTS</span></div>
  <div class="stat" style="left:501px"><strong>350</strong><span>PROJECTS<br>COMPLETED</span></div>
  <div class="stat" style="left:808px"><strong>106</strong><span>PARTNERS<br>WORLDWIDE</span></div>
  <svg class="abs" style="left:1145px;top:25px" width="36" height="36" viewBox="0 0 36 36"><path d="M4 4 L32 32 M32 4 L4 32" stroke="#1f1f1d" stroke-width="6"/></svg>
</section>

<!-- How we help -->
<div class="abs eyebrow" style="left:540px;top:3098px">We Work for you</div>
<h2 class="abs h-title section-center" style="top:3120px;font-size:30px">How We Help</h2>
<article class="help" style="left:224px"><span class="big">01</span><h3>CREATE</h3><p>I can help you figure out what makes you unique. It's your unique selling point that helps you stand out from the other millions of sites out there.</p><div class="more">KNOW MORE <i></i></div></article>
<article class="help" style="left:485px"><span class="big">02</span><h3>BUILD</h3><p>Your website is your own special place online for what you are trying to bring to the world. I help make it stand out and reflect everything you stand for.</p><div class="more">KNOW MORE <i></i></div></article>
<article class="help" style="left:745px"><span class="big">03</span><h3>MARKET</h3><p>Between SEO, SEM, social, blogging, &amp; email, web marketing can become overwhelming. I help you figure out the right path for you &amp; your growth.</p><div class="more">KNOW MORE <i></i></div></article>

<!-- Testimonials -->
<section class="band band-panel" style="top:3549px;height:390px">
  <div class="ghost-word" style="left:784px;top:16px;font-size:54px;color:var(--ghost-light)">TESTIMONIALS</div>
  <div class="abs" style="left:638px;top:36px;font-size:12px;color:var(--muted)">Feedback</div>
  <h2 class="abs h-title" style="left:224px;top:58px;font-size:28px">What Clients Say About Us</h2>
</section>
<div class="abs qmark">“”</div>
<p class="abs quote">“They are just awesome people. They are very creative and understand your needs. Marcus is very friendly and is full of very innovative ideas. Me and my team is very happy with the final result plus they are available for you 24/7. Thank you Marcus and</p>
<div class="abs photo" style="left:279px;top:3832px;width:38px;height:38px;border-radius:50%" role="img" aria-label="Client avatar"></div>
<div class="abs" style="left:332px;top:3834px"><div style="font-family:var(--head);font-weight:800;font-size:14px">Theo Brannick</div><div style="font-size:11.5px;color:var(--muted);margin-top:4px">CEO at Larkfield</div></div>
<svg class="abs" style="left:574px;top:3830px" width="40" height="16" viewBox="0 0 40 16"><path d="M8 2 L2 8 L8 14" fill="none" stroke="#fff" stroke-width="2"/><path d="M30 2 L36 8 L30 14" fill="none" stroke="#f2b21d" stroke-width="2"/></svg>
<div class="dots" style="left:560px;top:3862px"><span></span><span class="on"></span><span></span><span></span></div>
<div class="avatar photo gold" style="left:741px;top:3716px" role="img" aria-label="Client portrait"></div>
<div class="avatar photo" style="left:828px;top:3690px" role="img" aria-label="Client portrait"></div>
<div class="avatar photo gold" style="left:909px;top:3666px;width:65px;height:65px" role="img" aria-label="Client portrait"></div>
<div class="avatar photo" style="left:828px;top:3771px" role="img" aria-label="Client portrait"></div>
<div class="avatar photo" style="left:909px;top:3755px" role="img" aria-label="Client portrait"></div>
<div class="avatar photo gold" style="left:741px;top:3812px" role="img" aria-label="Client portrait"></div>
<div class="avatar photo" style="left:828px;top:3848px" role="img" aria-label="Client portrait"></div>
<div class="avatar photo gold" style="left:909px;top:3834px;width:65px;height:65px" role="img" aria-label="Client portrait"></div>

<!-- Team -->
<div class="ghost-word" style="left:22px;top:4048px;font-size:110px">TEAM</div>
<div class="abs eyebrow" style="left:780px;top:4034px">10+ Years Experience</div>
<h2 class="abs h-title" style="left:685px;top:4056px;font-size:28px">Experts For You</h2>
<div class="member" style="left:224px"><div class="pic photo" role="img" aria-label="Team member portrait in a suit"><div class="soc"><i></i><i></i><i></i><i></i></div></div><h4>ADAM CORRIN</h4><small>UI/UX</small></div>
<div class="member" style="left:485px"><div class="pic photo" role="img" aria-label="Team member portrait in a blazer"><div class="soc"><i></i><i></i><i></i><i></i></div></div><h4>LUCAS PEMBRY</h4><small>Senior Developer</small></div>
<div class="member" style="left:745px"><div class="pic photo" role="img" aria-label="Team member portrait in a suit and tie"><div class="soc"><i></i><i></i><i></i><i></i></div></div><h4>NOLAN AVERY</h4><small>Manager</small></div>

<!-- Contact -->
<div class="band band-panel" style="top:4783px;height:421px"></div>
<section class="abs contact">
  <h2>GET FREE AUDIT &amp; CONSULTATION</h2>
  <p class="lead">Get in touch with us and get started</p>
  <div class="field" style="left:32px;top:107px;width:233px;height:37px">Full Name*</div>
  <div class="field" style="left:283px;top:107px;width:234px;height:37px">Phone Number*</div>
  <div class="field" style="left:32px;top:164px;width:233px;height:37px">Email Address*</div>
  <div class="field" style="left:283px;top:164px;width:234px;height:37px">Website Name</div>
  <div class="field" style="left:32px;top:218px;width:485px;height:105px">Message</div>
  <div class="submit">SUBMIT</div>
  <aside class="info">
    <div style="font-size:11.5px">Contact Information</div>
    <div class="row" style="top:128px"><svg width="12" height="14" viewBox="0 0 12 14"><path d="M6 14 C2 9 0 7 0 5 A6 6 0 0 1 12 5 C12 7 10 9 6 14Z" fill="#1f1f1d"/><circle cx="6" cy="5" r="2" fill="#f2b21d"/></svg><span>48 Fairview Lane,<br>Eastbrook, U.S</span></div>
    <div class="row" style="top:190px"><svg width="12" height="12" viewBox="0 0 12 12"><path d="M2 0 L5 3 L3 5 C4 7 5 8 7 9 L9 7 L12 10 L10 12 C5 12 0 7 0 2Z" fill="#1f1f1d"/></svg><span>555-014-2290</span></div>
    <div class="row" style="top:234px"><svg width="13" height="10" viewBox="0 0 13 10"><rect width="13" height="10" fill="#1f1f1d"/><path d="M0 0 L6.5 5 L13 0" fill="none" stroke="#f2b21d"/></svg><span>hello@vordale.example</span></div>
    <div class="logo" style="position:absolute;left:58px;top:340px;color:#fff;font-size:19px">VORDALE<small>STUDIO</small></div>
  </aside>
</section>

<!-- Footer -->
<footer>
  <div class="footer-col" style="left:224px;top:5008px">
    <div class="logo" style="font-size:19px">VORDALE<small>STUDIO</small></div>
    <div style="margin-top:14px;line-height:17px;font-size:11.5px">Lorem ipsum dolor sit<br>amet, consectetur</div>
    <div style="margin-top:16px;display:flex;gap:12px"><span class="circle"></span><span class="circle"></span><span class="circle"></span></div>
  </div>
  <div class="footer-col" style="left:414px"><h5>QUICK LINKS</h5>Home<br>About<br>Services<br>Blog</div>
  <div class="footer-col" style="left:572px"><h5>POLICIES</h5>Privacy Policy<br>Terms &amp; Conditions<br>Disclaimer</div>
  <div class="footer-col" style="left:762px;width:212px"><h5>NEWSLETTER</h5><div style="line-height:18px">Subscribe to our Newsletter to get latest updates and news.</div>
    <div style="margin-top:20px;display:flex;height:31px"><div style="flex:1;background:#fff;color:#999;font-size:9.5px;padding:0 10px;display:flex;align-items:center">Enter Your Email Address</div><div style="width:72px;background:var(--gold);color:var(--ink);font-family:var(--head);font-weight:800;font-size:9.5px;display:flex;align-items:center;justify-content:center">SUBSCRIBE</div></div>
  </div>
  <div class="abs" style="left:0;top:5166px;width:1200px;height:38px;border-top:1px solid #4a4a45;text-align:center;font-size:11px;line-height:38px;color:#e0e0dc">©2021 VORDALE | All Rights Reserved</div>
</footer>

</body>
</html>
```